Income Tax Flyer - Updates Needed

Just need to update this flyer design and give it a new look. We would like to keep all the same wording but make it stand out a little more. Our selling point is the "Same Day Tax Advance up to $6,000"

Industry/Entity Type

Lending, Small Loans, Tax Services, Title Loans, Personal Loans

```html
<!DOCTYPE html>
<html lang="en">
<head>
<meta charset="utf-8">
<title>Same Day Tax Advance Flyer</title>
<link href="https://fonts.googleapis.com/css2?family=Cinzel:wght@700&family=Roboto:wght@400;700&family=Roboto+Condensed:wght@700&display=swap" rel="stylesheet">
<style>
  :root {
    --green: #05492a;
    --green-deep: #043d21;
    --red: #bb0b27;
    --white: #ffffff;
    --photo-light: #e3e6e6;
    --photo-mid: #b9b3ad;
    --photo-warm: #9a6f55;
    --photo-dark: #4a4440;
  }
  * { margin: 0; padding: 0; box-sizing: border-box; }
  html, body { width: 927px; height: 1200px; overflow: hidden; background: var(--green); }
  .flyer { position: relative; width: 927px; height: 1200px; background: var(--green); color: var(--white); font-family: "Roboto", sans-serif; overflow: hidden; }
  .backdrop { position: absolute; inset: 0; }
  .headline { position: absolute; top: 38px; left: 0; width: 100%; text-align: center; font-family: "Cinzel", serif; font-weight: 700; line-height: 80px; }
  .headline span { display: block; }
  .headline .line-top { font-size: 84px; letter-spacing: 1px; }
  .headline .amount { font-size: 86px; color: var(--red); }
  .headline .line-bottom { font-size: 86px; }
  .tagline { position: absolute; top: 316px; width: 100%; text-align: center; font-family: "Roboto Condensed", sans-serif; font-weight: 700; font-size: 30px; }
  .steps { position: absolute; top: 385px; left: 0; width: 927px; height: 180px; }
  .step-line { position: absolute; top: 46px; left: 169px; width: 597px; height: 5px; background: var(--white); }
  .step { position: absolute; width: 240px; text-align: center; }
  .step .badge { width: 96px; height: 96px; border-radius: 50%; background: var(--white); margin: 0 auto; display: flex; align-items: center; justify-content: center; }
  .step .badge.is-accent { background: var(--red); }
  .step p { margin-top: 22px; font-family: "Roboto Condensed", sans-serif; font-weight: 700; font-size: 24px; line-height: 35px; }
  .contact-title { position: absolute; top: 672px; left: 38px; font-family: "Roboto Condensed", sans-serif; font-weight: 700; font-size: 39px; line-height: 45px; }
  .contact-title span { display: inline-block; border-bottom: 2px solid var(--white); }
  .contact-phone { position: absolute; top: 677px; left: 312px; display: flex; align-items: center; gap: 9px; font-family: "Roboto Condensed", sans-serif; font-weight: 700; font-size: 30px; }
  .contact-address { position: absolute; top: 674px; left: 636px; display: flex; gap: 10px; font-size: 22px; line-height: 36px; }
  .photo { position: absolute; left: 0; top: 0; }
  .brand { position: absolute; left: 28px; top: 968px; color: var(--green); font-family: "Roboto", sans-serif; font-weight: 700; font-size: 44px; line-height: 50px; display: flex; align-items: center; gap: 14px; }
  .brand .mark { width: 26px; height: 26px; background: var(--green); border-radius: 50%; flex: none; }
  .offer-band { position: absolute; bottom: 0; left: 0; width: 927px; height: 55px; }
  .offer-band p { position: absolute; top: 0; left: 0; width: 886px; text-align: center; font-family: "Roboto Condensed", sans-serif; font-weight: 700; font-size: 40px; line-height: 55px; }
</style>
</head>
<body>
<main class="flyer">
  <svg class="backdrop" width="927" height="1200" viewBox="0 0 927 1200" aria-hidden="true">
    <path d="M0 660 Q60 610 300 604 L470 610 Q520 600 650 604 Q870 610 927 660 L927 1200 L0 1200 Z" fill="var(--green-deep)"/>
  </svg>

  <h1 class="headline">
    <span class="line-top">APPLY HERE FOR</span>
    <span class="amount">$5,000-$6,000</span>
    <span class="line-bottom">TODAY!</span>
  </h1>

  <p class="tagline">File your taxes and apply for an Easy Advance!</p>

  <section class="steps">
    <div class="step-line"></div>
    <div class="step" style="left:49px;">
      <div class="badge is-accent">
        <svg width="62" height="62" viewBox="0 0 62 62" aria-hidden="true">
          <path d="M31 4 A27 27 0 1 1 8 17" fill="none" stroke="#fff" stroke-width="2.5" stroke-dasharray="5 4"/>
          <path d="M44 6 L50 10 L44 14" fill="none" stroke="#fff" stroke-width="2.5"/>
          <text x="31" y="38" text-anchor="middle" font-family="Roboto, sans-serif" font-weight="700" font-size="18" fill="#fff">24/7</text>
        </svg>
      </div>
      <p>Available in<br>24 hours or Less</p>
    </div>
    <div class="step" style="left:337px;">
      <div class="badge">
        <svg width="56" height="56" viewBox="0 0 56 56" aria-hidden="true">
          <rect x="8" y="6" width="32" height="42" rx="2" fill="none" stroke="var(--red)" stroke-width="2.5"/>
          <text x="24" y="17" text-anchor="middle" font-family="Roboto, sans-serif" font-weight="700" font-size="9" fill="var(--red)">LOAN</text>
          <path d="M13 24 H32 M13 30 H30 M13 36 H26" stroke="var(--red)" stroke-width="2.5"/>
          <path d="M34 40 L48 14 L52 17 L38 42 Z" fill="none" stroke="var(--red)" stroke-width="2.5"/>
        </svg>
      </div>
      <p>Choose your Loan<br>Amount</p>
    </div>
    <div class="step" style="left:646px;">
      <div class="badge">
        <svg width="64" height="64" viewBox="0 0 64 64" aria-hidden="true">
          <circle cx="36" cy="36" r="20" fill="none" stroke="var(--red)" stroke-width="3"/>
          <circle cx="36" cy="36" r="14" fill="none" stroke="var(--red)" stroke-width="2"/>
          <path d="M36 28 V36 L42 40" fill="none" stroke="var(--red)" stroke-width="3"/>
          <rect x="31" y="6" width="10" height="6" fill="var(--red)"/>
          <path d="M36 12 V16" stroke="var(--red)" stroke-width="3"/>
          <path d="M4 30 H14 M2 37 H12 M6 44 H15" stroke="var(--red)" stroke-width="2.5"/>
        </svg>
      </div>
      <p>Quick and Easy</p>
    </div>
  </section>

  <h2 class="contact-title"><span>Contact Us&nbsp;</span><br><span>Today!</span></h2>

  <div class="contact-phone">
    <svg width="40" height="40" viewBox="0 0 40 40" aria-hidden="true">
      <circle cx="20" cy="20" r="20" fill="var(--red)"/>
      <path d="M13 10 L17 10 L19 16 L16 18 Q19 24 23 25 L25 22 L31 24 L31 28 Q30 31 26 31 Q12 28 9 14 Q9 10 13 10 Z" fill="#fff"/>
    </svg>
    <span>+1 888 888 8888</span>
  </div>

  <div class="contact-address">
    <svg width="22" height="30" viewBox="0 0 22 30" aria-hidden="true" style="margin-top:6px;">
      <path d="M11 0 A11 11 0 0 1 22 11 C22 19 11 30 11 30 C11 30 0 19 0 11 A11 11 0 0 1 11 0 Z" fill="#fff"/>
      <circle cx="11" cy="11" r="4.5" fill="var(--green-deep)"/>
    </svg>
    <p>123,Duis aute irure dol<br>orreprehenderit</p>
  </div>

  <svg class="photo" width="927" height="1200" viewBox="0 0 927 1200">
    <defs>
      <linearGradient id="photoTone" x1="0" y1="0" x2="1" y2="0.4">
        <stop offset="0" stop-color="var(--photo-light)"/>
        <stop offset="0.45" stop-color="var(--photo-mid)"/>
        <stop offset="0.8" stop-color="var(--photo-warm)"/>
        <stop offset="1" stop-color="var(--photo-dark)"/>
      </linearGradient>
      <radialGradient id="photoShade" cx="0.62" cy="0.85" r="0.45">
        <stop offset="0" stop-color="var(--photo-dark)" stop-opacity="0.55"/>
        <stop offset="1" stop-color="var(--photo-dark)" stop-opacity="0"/>
      </radialGradient>
    </defs>
    <path d="M0 922 Q470 655 927 922 L927 1200 L0 1200 Z" fill="var(--red)"/>
    <path d="M0 946 Q470 705 927 946 L927 1200 L0 1200 Z" fill="#fff"/>
    <g role="img" aria-label="Photo of two business professionals discussing paperwork at an office desk">
      <path d="M0 954 Q470 723 927 954 L927 1200 L0 1200 Z" fill="url(#photoTone)"/>
      <path d="M0 954 Q470 723 927 954 L927 1200 L0 1200 Z" fill="url(#photoShade)"/>
    </g>
  </svg>

  <div class="brand"><span class="mark"></span><span>Keystone<br>Financial Group</span></div>

  <div class="offer-band">
    <svg width="927" height="55" viewBox="0 0 927 55" aria-hidden="true" style="position:absolute;left:0;top:0;">
      <path d="M48 0 H927 V55 H0 Z" fill="var(--red)"/>
    </svg>
    <p>Same Day Tax Advance up to $6,000</p>
  </div>
</main>
</body>
</html>
```